Creative Fitness Studio Feature Wall

Two feature walls within functional fitness studio, they need to be on brand and have a WOW factor.
Designed to inspire and motivate people to live a fit and healthy lifestyle whilst working out and bringing life to the studio, as an uplifting and inviting environment.

Please see current walls and also visit website www.velta4.com.au for inspiration.
Updates

Target Market(s)

health and fitness, healthy lifestyle

Industry/Entity Type

Fitness

Font styles to use
Other font styles liked:
• gothic

Colors

Designer to choose colors to be used in the design.

Requirements
Must have
• inspiration from website www.velta4.com.au ........... brand consistency
Nice to have
• WOW factor......... walk into the gym and it draws your attention.
Should not have
• Overly muscly people (bodybuilders)

```html
<!DOCTYPE html>
<html lang="en">
<head>
<meta charset="utf-8">
<title>Velta4 Fitness – Feature Wall</title>
<link href="https://fonts.googleapis.com/css2?family=Bebas+Neue&family=Montserrat:wght@500;700&display=swap" rel="stylesheet">
<style>
  :root {
    --brand-green: #8cc63f;
    --ink: #111111;
    --paper: #ffffff;
  }
  html, body {
    margin: 0;
    padding: 0;
    width: 1200px;
    height: 1200px;
    overflow: hidden;
    background: var(--paper);
  }
  .feature-wall {
    display: block;
    width: 1200px;
    height: 1200px;
  }
  .display-type { font-family: 'Bebas Neue', 'Oswald', sans-serif; }
  .web-type { font-family: 'Montserrat', 'Helvetica Neue', sans-serif; }
  .wordmark { fill: var(--ink); }
  .headline { fill: var(--paper); }
  .quote-green { fill: var(--brand-green); }
  .quote-ink { fill: var(--ink); }
  .quote-white { fill: var(--paper); }
  .tagline { fill: var(--ink); }
  .url-base { fill: var(--ink); }
  .url-accent { fill: var(--brand-green); font-weight: 700; }
  .green-panel { fill: var(--brand-green); }
  .black-corner { fill: var(--ink); }
</style>
</head>
<body>
<svg class="feature-wall" viewBox="0 0 1000 1000" xmlns="http://www.w3.org/2000/svg">
  <defs>
    <linearGradient id="tone-pushup" x1="0" y1="0" x2="1" y2="1">
      <stop offset="0" stop-color="#1c1c1c"/>
      <stop offset="0.45" stop-color="#8a3a2c"/>
      <stop offset="1" stop-color="#161616"/>
    </linearGradient>
    <linearGradient id="tone-boxing" x1="0" y1="0" x2="1" y2="1">
      <stop offset="0" stop-color="#b3201c"/>
      <stop offset="0.55" stop-color="#5a2a22"/>
      <stop offset="1" stop-color="#141414"/>
    </linearGradient>
    <radialGradient id="tone-kettlebell" cx="0.5" cy="0.45" r="0.65">
      <stop offset="0" stop-color="#8a6a58"/>
      <stop offset="0.6" stop-color="#4a3a34"/>
      <stop offset="1" stop-color="#1d1a19"/>
    </radialGradient>
    <linearGradient id="tone-medball" x1="0" y1="0" x2="1" y2="1">
      <stop offset="0" stop-color="#2c3b63"/>
      <stop offset="1" stop-color="#121212"/>
    </linearGradient>
    <linearGradient id="tone-stability" x1="0" y1="0" x2="1" y2="1">
      <stop offset="0" stop-color="#f2efec"/>
      <stop offset="0.5" stop-color="#c7b3a6"/>
      <stop offset="1" stop-color="#8e8e92"/>
    </linearGradient>
    <radialGradient id="tone-climbers" cx="0.5" cy="0.4" r="0.7">
      <stop offset="0" stop-color="#6a5a4c"/>
      <stop offset="0.6" stop-color="#2e2e2e"/>
      <stop offset="1" stop-color="#141414"/>
    </radialGradient>
    <linearGradient id="tone-dumbbell" x1="0" y1="0" x2="1" y2="1">
      <stop offset="0" stop-color="#f4f4f6"/>
      <stop offset="0.5" stop-color="#e3c6b4"/>
      <stop offset="1" stop-color="#2f5fb8"/>
    </linearGradient>
    <linearGradient id="tone-barbell" x1="0" y1="0" x2="1" y2="1">
      <stop offset="0" stop-color="#f0e6dc"/>
      <stop offset="0.5" stop-color="#d4b294"/>
      <stop offset="1" stop-color="#2a2a2a"/>
    </linearGradient>
  </defs>

  <!-- corner accent -->
  <polygon class="black-corner" points="0,0 140,0 140,92 0,172"/>

  <!-- brand wordmark -->
  <g class="brand">
    <text class="wordmark display-type" x="200" y="130" font-size="98" textLength="350" lengthAdjust="spacingAndGlyphs">VELTA4</text>
    <text class="wordmark display-type" x="272" y="161" font-size="28" textLength="193" lengthAdjust="spacing">FITNESS</text>
  </g>

  <!-- motivation panel -->
  <g class="motivation-panel">
    <polygon class="green-panel" points="150,135 352,250 352,482 150,598 0,512 0,220"/>
    <text class="headline display-type" x="38" y="278" font-size="66">MOTIVATION</text>
    <text class="headline display-type" x="38" y="314" font-size="37">IS WHAT GETS</text>
    <text class="headline display-type" x="38" y="348" font-size="37">YOU STARTED</text>
    <text class="headline display-type" x="38" y="419" font-size="66">HABIT</text>
    <text class="headline display-type" x="38" y="460" font-size="37">IS WHAT KEEPS YOU</text>
    <text class="headline display-type" x="38" y="516" font-size="66">GOING</text>
  </g>

  <!-- photo tiles -->
  <polygon role="img" aria-label="Woman doing an explosive push-up on a dark gym floor" fill="url(#tone-pushup)" points="612,0 785,0 785,214 612,114"/>
  <polygon role="img" aria-label="Woman in red boxing gloves throwing a punch" fill="url(#tone-boxing)" points="833,0 1000,0 1000,100 833,197"/>
  <polygon role="img" aria-label="Woman holding a kettlebell in a group fitness class" fill="url(#tone-kettlebell)" points="588,140 787,255 787,480 588,595 388,480 388,255"/>
  <polygon role="img" aria-label="Man doing push-ups on medicine balls" fill="url(#tone-medball)" points="860,244 1000,162 1000,332 880,262"/>
  <polygon role="img" aria-label="Woman training on a stability ball in a bright gym" fill="url(#tone-stability)" points="833,280 1000,376 1000,540 833,528"/>
  <polygon role="img" aria-label="Man and woman doing mountain climbers in a studio" fill="url(#tone-climbers)" points="362,530 562,644 562,874 362,988 165,874 165,644"/>
  <polygon role="img" aria-label="Smiling woman lifting blue dumbbells" fill="url(#tone-dumbbell)" points="612,672 785,772 785,985 612,985"/>
  <polygon role="img" aria-label="Smiling woman lifting a barbell with a personal trainer" fill="url(#tone-barbell)" points="833,790 1000,694 1000,985 833,985"/>

  <!-- quote over training tile -->
  <g class="photo-quote">
    <text class="quote-green display-type" x="363" y="831" font-size="46" text-anchor="middle">QUOTE WILL BE HERE</text>
    <text class="quote-white display-type" x="363" y="872" font-size="31" text-anchor="middle">HERE GETS HERE GETS</text>
    <text class="quote-white display-type" x="363" y="909" font-size="31" text-anchor="middle">YOU STARTEDYOU</text>
    <text class="quote-white display-type" x="363" y="946" font-size="31" text-anchor="middle">STARTED</text>
  </g>

  <!-- green quote panel -->
  <g class="quote-panel">
    <polygon class="green-panel" points="808,530 982,630 808,732 638,632"/>
    <text class="quote-ink display-type" x="805" y="609" font-size="48" text-anchor="middle">QUOTE</text>
    <text class="quote-white display-type" x="808" y="640" font-size="28" text-anchor="middle">HERE GETS HERE GETS</text>
    <text class="quote-white display-type" x="808" y="666" font-size="28" text-anchor="middle">YOU STARTEDYOU</text>
    <text class="quote-white display-type" x="808" y="692" font-size="28" text-anchor="middle">STARTED</text>
  </g>

  <!-- diagonal taglines -->
  <text class="tagline display-type" font-size="17" textLength="420" lengthAdjust="spacingAndGlyphs" transform="translate(622,134) rotate(30.3)">CHALLENGING YOURSELF EVERY DAY IS ONE OF THE MOST EXCITING WAYS TO LIVE.</text>
  <text class="tagline display-type" font-size="19" textLength="374" lengthAdjust="spacingAndGlyphs" transform="translate(428,545) rotate(29.5)">YOU'RE ONLY ONE WORKOUT AWAY FROM A GOOD MOOD</text>

  <!-- web address -->
  <text class="web-type" x="576" y="961" font-size="18" text-anchor="middle" font-weight="500"><tspan class="url-base">www.</tspan><tspan class="url-accent">velta4</tspan><tspan class="url-base">.com.au</tspan></text>
</svg>
</body>
</html>
```